Phuket Thailand - Andaman Stay Website

I have a villa for rent in Thailand and require a website - i need to demo pictures/walk through video, local attractions, villa facilities description plus seaonal rates and online booking.

Industry/Entity Type

Rental

Coding

Coded - Design and coding required

```html
<!DOCTYPE html>
<html lang="en">
<head>
<meta charset="utf-8">
<title>Andaman Stay – Phuket Villa Rentals</title>
<link href="https://fonts.googleapis.com/css2?family=Open+Sans:wght@300;400;600;700&family=Lobster&display=swap" rel="stylesheet">
<style>
:root{
  --orange:#f26722;
  --ink:#333333;
  --muted:#777777;
  --line:#e2e2e2;
  --gray-band:#ebebeb;
  --teal-btn:#7cc6de;
  --green-btn:#7ab317;
  --footer:#333333;
  --footer-text:#cfcfcf;
  --white:#ffffff;
}
*{box-sizing:border-box;margin:0;padding:0}
html,body{width:1200px;height:3084px;overflow:hidden}
body{font-family:"Open Sans",Arial,sans-serif;color:var(--ink);background:var(--white);position:relative}

/* Header */
.site-header{height:97px;position:relative}
.brand{position:absolute;left:103px;top:26px;display:flex;align-items:center;gap:10px;font-size:34px;font-weight:600;color:var(--orange)}
.brand-mark{width:14px;height:14px;background:var(--orange)}
.main-nav{position:absolute;left:386px;top:38px;display:flex;gap:20px;font-size:17px;color:#555}
.util{position:absolute;right:80px;top:0;display:flex;align-items:center;font-size:15px}
.util .wish{color:#555;margin-right:10px}
.util .btn{background:#dedede;color:#555;padding:4px 12px;border-left:1px solid #fff}
.phone{position:absolute;right:80px;top:40px;font-size:30px;color:var(--orange);font-weight:400}

/* Hero */
.hero{position:relative;height:610px;background:linear-gradient(160deg,#a9b7c0 0%,#6c7479 35%,#8a6d5b 60%,#4c5a3a 100%)}
.hero-copy{position:absolute;left:0;right:0;top:250px;text-align:center;color:var(--white)}
.hero-copy h1{font-family:"Lobster",cursive;font-weight:400;font-size:58px;line-height:1;text-shadow:0 2px 6px rgba(0,0,0,.5)}
.hero-copy p{font-size:40px;font-weight:400;margin-top:4px;text-shadow:0 2px 6px rgba(0,0,0,.5)}
.search{position:absolute;left:262px;top:548px;display:flex;gap:4px;height:41px}
.search .field{background:var(--white);font-size:14px;color:#999;padding:0 10px;display:flex;align-items:center;justify-content:space-between}
.search .where{width:232px;color:var(--ink)}
.search .date{width:115px}
.search .beds{width:106px;color:var(--ink)}
.search .go{width:88px;background:var(--green-btn);color:var(--white);font-weight:700;font-size:15px;display:flex;align-items:center;justify-content:center}

/* Section titles */
.section-title{text-align:center;font-size:24px;font-weight:400;text-transform:uppercase;color:var(--ink)}
.section-title b{font-weight:700}

/* Destinations */
.destinations{padding-top:60px;height:956px}
.villa-grid{position:absolute;left:85px;top:835px;display:grid;grid-template-columns:repeat(4,242px);column-gap:25px;row-gap:26px}
.villa-card{height:373px;border:1px solid var(--line);background:var(--white)}
.villa-photo{height:221px}
.villa-card h3{font-size:13px;font-weight:700;padding:14px 10px 0;line-height:1.35;height:72px}
.villa-rate{font-size:13px;color:var(--muted);padding:0 10px 10px;border-bottom:1px solid var(--line)}
.villa-foot{display:flex;align-items:center;justify-content:space-between;padding:10px 10px 0;font-size:13px;color:var(--muted)}
.villa-foot .loc{display:flex;align-items:center;gap:5px}
.villa-foot .details{background:var(--teal-btn);color:var(--white);font-size:12px;padding:7px 10px}
.p1{background:linear-gradient(#4f8fd8,#8fb5c9 55%,#2d9bd1)}
.p2{background:linear-gradient(#3b8be0,#9ac2de 50%,#3a7fb8)}
.p3{background:linear-gradient(#6da9e0,#8a7a62 50%,#2f8fb8)}
.p4{background:linear-gradient(#5ea4e6,#5f7a54 50%,#2c7fc9)}
.p5{background:linear-gradient(#5b9ee0,#dcdcdc 45%,#25a7a5)}
.p6{background:linear-gradient(#6f7fae,#d7a3a0 45%,#4a6f9c)}
.p7{background:linear-gradient(#2f6fd0,#4d7a3e 50%,#2f9fb9)}
.p8{background:linear-gradient(#7fb6e6,#c9b79c 50%,#5d7a50)}

/* Know us band */
.know{position:absolute;left:0;top:1663px;width:1200px;height:393px;background:var(--gray-band)}
.know .section-title{margin-top:52px}
.know-cols{display:flex;justify-content:space-between;padding:0 100px;margin-top:52px}
.know-item{width:300px;text-align:center}
.know-icon{height:72px;border-bottom:1px solid #d6d6d6;border-top:1px solid #d6d6d6;display:flex;align-items:center;justify-content:center;width:170px;margin:0 auto}
.know-item h4{font-size:14px;font-weight:700;margin-top:22px;text-transform:uppercase}
.know-item p{font-size:12.5px;color:var(--muted);line-height:1.6;margin-top:10px}

/* Difference */
.difference{position:absolute;left:0;top:2056px;width:1200px;height:355px}
.difference .section-title{margin-top:55px}
.diff-cols{display:flex;justify-content:space-between;padding:0 90px;margin-top:48px}
.diff-item{width:310px;text-align:center}
.diff-item h4{font-size:17px;font-weight:700;text-transform:uppercase;margin-top:14px}
.diff-item p{font-size:12.5px;color:var(--muted);line-height:1.6;margin-top:6px}

/* Video */
.video{position:absolute;left:0;top:2411px;width:1200px;height:411px;background:linear-gradient(90deg,#3a2a22 0%,#5a4536 30%,#2b2a28 55%,#6f6a5c 80%,#9a9a8c 100%)}
.video h2{position:absolute;left:0;right:0;top:135px;text-align:center;color:var(--white);font-size:32px;font-weight:700;text-transform:uppercase}
.play{position:absolute;left:568px;top:197px;width:96px;height:76px;background:var(--white);border-radius:16px;display:flex;align-items:center;justify-content:center}

/* Footer */
.site-footer{position:absolute;left:0;top:2822px;width:1200px;height:262px;background:var(--footer);border-top:5px solid var(--orange);color:var(--footer-text)}
.foot-nav{display:flex;justify-content:center;gap:30px;font-size:13px;text-transform:uppercase;padding:24px 0 22px;border-bottom:1px solid #4a4a4a;margin:0 240px}
.foot-cols{display:flex;padding:22px 0 0 85px;gap:0}
.foot-col h5{font-size:15px;font-weight:400;color:var(--white)}
.foot-col p{font-size:13px;line-height:1.5;margin-top:6px}
.social{width:270px}
.social-row{display:flex;gap:8px;margin-top:8px}
.social-row span{width:38px;height:38px;border:2px solid var(--white)}
.stay{width:355px}
.signup{display:flex;margin-top:12px}
.signup .email{width:190px;height:38px;background:#555;color:#bbb;font-size:13px;padding:0 12px;display:flex;align-items:center}
.signup .btn{width:100px;height:38px;background:#4a4a4a;color:var(--white);font-size:14px;display:flex;align-items:center;justify-content:center}
.who{width:420px}
.copyright{position:absolute;left:85px;right:85px;bottom:10px;display:flex;justify-content:space-between;font-size:12px}
.copyright .legal{display:flex;gap:24px}
</style>
</head>
<body>

<header class="site-header">
  <div class="brand"><span class="brand-mark"></span>Andaman Stay</div>
  <nav class="main-nav"><span>Home</span><span>About</span><span>Destinations</span><span>Featured Villas</span><span>Contact</span></nav>
  <div class="util"><span class="wish">Your Wish List</span><span class="btn">Sign Up</span><span class="btn">Login</span></div>
  <div class="phone">1-800-555-0147</div>
</header>

<section class="hero" role="img" aria-label="Modern villa exterior with tiled roof and tropical garden">
  <div class="hero-copy">
    <h1>Lorem ipsum dolor sit amet</h1>
    <p>consectetur adipiscing elit</p>
  </div>
  <form class="search">
    <div class="field where">Phuket, Thailand</div>
    <div class="field date">Check in
      <svg width="16" height="16" viewBox="0 0 16 16"><rect x="1" y="3" width="14" height="12" fill="none" stroke="#999"/><line x1="1" y1="6" x2="15" y2="6" stroke="#999"/></svg></div>
    <div class="field date">Check out
      <svg width="16" height="16" viewBox="0 0 16 16"><rect x="1" y="3" width="14" height="12" fill="none" stroke="#999"/><line x1="1" y1="6" x2="15" y2="6" stroke="#999"/></svg></div>
    <div class="field beds">Bedrooms <svg width="10" height="6" viewBox="0 0 10 6"><path d="M0 0h10L5 6z" fill="#555"/></svg></div>
    <div class="go">SEARCH</div>
  </form>
</section>

<section class="destinations">
  <h2 class="section-title">Popular <b>Destinations</b></h2>
</section>
<div class="villa-grid">
  <article class="villa-card"><div class="villa-photo p1" role="img" aria-label="Villa with infinity pool"></div><h3>Lorem ipsum dolor sit amet consectetur</h3><div class="villa-rate">$850 - $2,950 /night</div><div class="villa-foot"><span class="loc"><svg width="12" height="16" viewBox="0 0 12 16"><path d="M6 0a6 6 0 0 0-6 6c0 4 6 10 6 10s6-6 6-10a6 6 0 0 0-6-6z" fill="#f5a623"/><circle cx="6" cy="6" r="2.2" fill="#fff"/></svg>Lorem Ipsum</span><span class="details">VIEW DETAILS</span></div></article>
  <article class="villa-card"><div class="villa-photo p2" role="img" aria-label="Pool terrace with sun loungers"></div><h3>Lorem ipsum dolor sit amet consectetur</h3><div class="villa-rate">$850 - $2,950 /night</div><div class="villa-foot"><span class="loc"><svg width="12" height="16" viewBox="0 0 12 16"><path d="M6 0a6 6 0 0 0-6 6c0 4 6 10 6 10s6-6 6-10a6 6 0 0 0-6-6z" fill="#f5a623"/><circle cx="6" cy="6" r="2.2" fill="#fff"/></svg>Lorem Ipsum</span><span class="details">VIEW DETAILS</span></div></article>
  <article class="villa-card"><div class="villa-photo p3" role="img" aria-label="Thai-style villa beside a pool"></div><h3>Lorem ipsum dolor sit amet consectetur</h3><div class="villa-rate">$850 - $2,950 /night</div><div class="villa-foot"><span class="loc"><svg width="12" height="16" viewBox="0 0 12 16"><path d="M6 0a6 6 0 0 0-6 6c0 4 6 10 6 10s6-6 6-10a6 6 0 0 0-6-6z" fill="#f5a623"/><circle cx="6" cy="6" r="2.2" fill="#fff"/></svg>Lorem Ipsum</span><span class="details">VIEW DETAILS</span></div></article>
  <article class="villa-card"><div class="villa-photo p4" role="img" aria-label="Hillside villa with blue pool"></div><h3>Lorem ipsum dolor sit amet consectetur</h3><div class="villa-rate">$850 - $2,950 /night</div><div class="villa-foot"><span class="loc"><svg width="12" height="16" viewBox="0 0 12 16"><path d="M6 0a6 6 0 0 0-6 6c0 4 6 10 6 10s6-6 6-10a6 6 0 0 0-6-6z" fill="#f5a623"/><circle cx="6" cy="6" r="2.2" fill="#fff"/></svg>Lorem Ipsum</span><span class="details">VIEW DETAILS</span></div></article>
  <article class="villa-card"><div class="villa-photo p5" role="img" aria-label="White villa with turquoise pool"></div><h3>Lorem ipsum dolor sit amet consectetur</h3><div class="villa-rate">$850 - $2,950 /night</div><div class="villa-foot"><span class="loc"><svg width="12" height="16" viewBox="0 0 12 16"><path d="M6 0a6 6 0 0 0-6 6c0 4 6 10 6 10s6-6 6-10a6 6 0 0 0-6-6z" fill="#f5a623"/><circle cx="6" cy="6" r="2.2" fill="#fff"/></svg>Lorem Ipsum</span><span class="details">VIEW DETAILS</span></div></article>
  <article class="villa-card"><div class="villa-photo p6" role="img" aria-label="Infinity pool at dusk over the sea"></div><h3>Lorem ipsum dolor sit amet consectetur</h3><div class="villa-rate">$850 - $2,950 /night</div><div class="villa-foot"><span class="loc"><svg width="12" height="16" viewBox="0 0 12 16"><path d="M6 0a6 6 0 0 0-6 6c0 4 6 10 6 10s6-6 6-10a6 6 0 0 0-6-6z" fill="#f5a623"/><circle cx="6" cy="6" r="2.2" fill="#fff"/></svg>Lorem Ipsum</span><span class="details">VIEW DETAILS</span></div></article>
  <article class="villa-card"><div class="villa-photo p7" role="img" aria-label="Tropical garden pool with palm trees"></div><h3>Lorem ipsum dolor sit amet consectetur</h3><div class="villa-rate">$850 - $2,950 /night</div><div class="villa-foot"><span class="loc"><svg width="12" height="16" viewBox="0 0 12 16"><path d="M6 0a6 6 0 0 0-6 6c0 4 6 10 6 10s6-6 6-10a6 6 0 0 0-6-6z" fill="#f5a623"/><circle cx="6" cy="6" r="2.2" fill="#fff"/></svg>Lorem Ipsum</span><span class="details">VIEW DETAILS</span></div></article>
  <article class="villa-card"><div class="villa-photo p8" role="img" aria-label="Multi-level villa with sea view"></div><h3>Lorem ipsum dolor sit amet consectetur</h3><div class="villa-rate">$850 - $2,950 /night</div><div class="villa-foot"><span class="loc"><svg width="12" height="16" viewBox="0 0 12 16"><path d="M6 0a6 6 0 0 0-6 6c0 4 6 10 6 10s6-6 6-10a6 6 0 0 0-6-6z" fill="#f5a623"/><circle cx="6" cy="6" r="2.2" fill="#fff"/></svg>Lorem Ipsum</span><span class="details">VIEW DETAILS</span></div></article>
</div>

<section class="know">
  <h2 class="section-title">3 Things <b>You Should Know</b> About Us</h2>
  <div class="know-cols">
    <div class="know-item">
      <div class="know-icon"><svg width="44" height="44" viewBox="0 0 44 44"><circle cx="22" cy="22" r="20" fill="#8a8a8a"/><path d="M22 10l3.6 7.6 8.2 1-6 5.6 1.6 8.2L22 28.4l-7.4 4 1.6-8.2-6-5.6 8.2-1z" fill="#ebebeb"/></svg></div>
      <h4>Quality, Assured.</h4>
      <p>Lorem ipsum dolor sit amet, consectetur adipiscing elit, sed do eiusmod tempor incididunt ut labore et dolore magna aliqua. Ut enim ad minim veniam, quis nostrud exercitation.</p>
    </div>
    <div class="know-item">
      <div class="know-icon"><svg width="48" height="44" viewBox="0 0 48 44"><path d="M24 2L2 22h6v20h12V30h8v12h12V22h6z" fill="#8a8a8a"/></svg></div>
      <h4>The Perfect Match</h4>
      <p>Lorem ipsum dolor sit amet, consectetur adipiscing elit, sed do eiusmod tempor incididunt ut labore et dolore magna aliqua. Ut enim ad minim veniam, quis nostrud exercitation.</p>
    </div>
    <div class="know-item">
      <div class="know-icon"><svg width="44" height="44" viewBox="0 0 44 44"><path d="M36 12A17 17 0 1 0 39 22" fill="none" stroke="#8a8a8a" stroke-width="4"/><path d="M32 4l6 8-9 2z" fill="#8a8a8a"/><path d="M22 12v10l7 5" fill="none" stroke="#8a8a8a" stroke-width="4"/></svg></div>
      <h4>At Your Service 24/7</h4>
      <p>Lorem ipsum dolor sit amet, consectetur adipiscing elit, sed do eiusmod tempor incididunt ut labore et dolore magna aliqua. Ut enim ad minim veniam, quis nostrud exercitation.</p>
    </div>
  </div>
</section>

<section class="difference">
  <h2 class="section-title">The Andaman Stay <b>Difference</b></h2>
  <div class="diff-cols">
    <div class="diff-item">
      <svg width="60" height="60" viewBox="0 0 60 60"><circle cx="30" cy="30" r="27" fill="none" stroke="#f26722" stroke-width="4"/><circle cx="21" cy="24" r="3" fill="#f26722"/><circle cx="39" cy="24" r="3" fill="#f26722"/><path d="M17 35q13 13 26 0" fill="none" stroke="#f26722" stroke-width="4" stroke-linecap="round"/></svg>
      <h4>99% Customer Satisfaction</h4>
      <p>Lorem ipsum dolor sit amet, consectetur adipiscing elit, sed do eiusmod tempor incididunt</p>
    </div>
    <div class="diff-item">
      <svg width="60" height="60" viewBox="0 0 60 60"><circle cx="30" cy="30" r="27" fill="none" stroke="#f26722" stroke-width="4"/><text x="30" y="37" text-anchor="middle" font-family="Open Sans, sans-serif" font-size="19" font-weight="700" fill="#f26722">25+</text></svg>
      <h4>Over 25 Years Experience</h4>
      <p>Lorem ipsum dolor sit amet, consectetur adipiscing elit, sed do eiusmod tempor incididunt</p>
    </div>
    <div class="diff-item">
      <svg width="60" height="60" viewBox="0 0 60 60"><rect x="12" y="8" width="32" height="44" rx="3" fill="none" stroke="#f26722" stroke-width="4"/><rect x="21" y="4" width="14" height="8" fill="#f26722"/><path d="M18 22h16M18 30h12M18 38h10" stroke="#f26722" stroke-width="3"/><path d="M36 40l5 5 10-11" fill="none" stroke="#f26722" stroke-width="4"/></svg>
      <h4>Personally Inspected Villas</h4>
      <p>Lorem ipsum dolor sit amet, consectetur adipiscing elit, sed do eiusmod tempor incididunt</p>
    </div>
  </div>
</section>

<section class="video" role="img" aria-label="Villa interior walk-through video still showing living room and bedroom">
  <h2>Watch Video</h2>
  <div class="play"><svg width="34" height="38" viewBox="0 0 34 38"><path d="M2 2l30 17L2 36z" fill="#222"/></svg></div>
</section>

<footer class="site-footer">
  <nav class="foot-nav"><span>Home</span><span>About Us</span><span>Destinations</span><span>Featured Villas</span><span>Contact Us</span></nav>
  <div class="foot-cols">
    <div class="foot-col social">
      <h5>Let's Socialize</h5>
      <p>Follow us:</p>
      <div class="social-row"><span aria-label="Social profile"></span><span aria-label="Social profile"></span><span aria-label="Social profile"></span><span aria-label="Social profile"></span></div>
    </div>
    <div class="foot-col stay">
      <h5>Stay in the Know</h5>
      <p>Exclusive news &amp; offers straight to your inbox:</p>
      <div class="signup"><span class="email">Enter email address...</span><span class="btn">SIGN UP</span></div>
    </div>
    <div class="foot-col who">
      <h5>Who we are</h5>
      <p>Cras tempus nisi id urna vestibulum ullamcorper. Cras nibh nibh, dignissim sit amet ultricies vel, mattis sit amet elit. Praesent ipsum augue, dictum ut porttitor sit amet, feugiat vitae lorem eleifend vulputate libero, at volutpat ante viverra.</p>
    </div>
  </div>
  <div class="copyright"><span>Copyright ©2015 Andaman Stay. All Rights Reserved.</span><span class="legal"><span>Privacy policy</span><span>Terms of use</span></span></div>
</footer>

</body>
</html>
```